Letterhead Design Project

Consulting Company , we want a letterhead incorporating both the picture provided and the logo provided. The font name is monotype corsiva.
Target Market(s)
Dentist
Industry/Entity Type
Consulting
Font styles to use
Other font styles liked:
- monotype corsiva

Colors
0455a3
Requirements
Must have
- the logo, the picture (see attached), the website name, the email. and the phone numbers.
- Website: www.trquillarisadvisory.solutions
- Email: will be provided to the winner, please use placeholder
- Phone numbers:
- Petra Hallum 5829017763
- Owen Vrastik 6148250397

Nice to have
- a swoop or wave across the bottom. a line up the side. I don't know guys. design something unique and professional.

Should not have
- arrows pointing off the logo or anywhere. no arrows. our logo altered in anyway. no broken circles. no variences in blue. we like our logo the way it is. the font is monotype corsiva

```html
<!DOCTYPE html>
<html lang="en">
<head>
<meta charset="utf-8">
<title>Trquillaris Advisory Letterhead</title>
<link rel="stylesheet" href="https://fonts.googleapis.com/css2?family=Cormorant+Garamond:ital,wght@1,500&display=swap">
<style>
  :root {
    --backdrop: #d9d9d9;
    --paper: #ffffff;
    --brand-blue: #0455a3;
    --ink-dark: #333a3f;
    --ring-grey: #7d8589;
  }
  * { margin: 0; padding: 0; box-sizing: border-box; }
  html, body {
    width: 1200px; height: 896px; overflow: hidden;
    background: var(--backdrop);
  }
  .letterhead {
    position: absolute; left: 296px; top: 18px;
    width: 608px; height: 860px;
    background: var(--paper);
    box-shadow: 0 2px 10px rgba(0,0,0,0.12);
    font-family: "Cormorant Garamond", "Times New Roman", serif;
    font-style: italic; font-weight: 500;
  }
  .header-rules, .footer-rules { position: absolute; left: 0; width: 608px; }
  .header-rules { top: 0; height: 120px; }
  .footer-rules { bottom: 0; height: 120px; }
  .brand-mark {
    position: absolute; left: 34px; top: 40px;
    width: 64px; height: 64px; border-radius: 50%;
    border: 3px solid var(--ring-grey);
  }
  .company-name {
    position: absolute; left: 112px; top: 70px;
    font-size: 25px; font-weight: 500; color: var(--brand-blue); white-space: nowrap;
  }
  .company-address {
    position: absolute; left: 114px; top: 102px;
    font-size: 12px; line-height: 13px; color: var(--ink-dark);
    font-style: italic;
  }
  .contact-block {
    position: absolute; left: 36px; bottom: 58px;
    display: flex; flex-direction: column; gap: 6px;
    font-size: 12px; color: var(--ink-dark);
  }
  .contact-row { display: flex; gap: 38px; align-items: center; }
  .contact-item { display: flex; align-items: center; gap: 6px; white-space: nowrap; }
  .contact-item svg { width: 11px; height: 11px; flex: none; }
</style>
</head>
<body>
<main class="letterhead">
  <svg class="header-rules" viewBox="0 0 608 120" aria-hidden="true">
    <g stroke="var(--brand-blue)" stroke-width="1.6" fill="none">
      <line x1="100" y1="48" x2="236" y2="48"/>
      <line x1="100" y1="56" x2="306" y2="56"/>
      <line x1="100" y1="64" x2="376" y2="64"/>
    </g>
  </svg>

  <div class="brand-mark"></div>
  <h1 class="company-name">Trquillaris Advisory, LLC</h1>
  <address class="company-address">418 Larkspur Lane<br>Alder Bend, Kentucky 40917</address>

  <div class="contact-block">
    <div class="contact-row">
      <span class="contact-item">
        <svg viewBox="0 0 12 12"><circle cx="6" cy="6" r="5" fill="none" stroke="var(--brand-blue)"/><path d="M1 6h10M6 1c-3 3-3 7 0 10M6 1c3 3 3 7 0 10" fill="none" stroke="var(--brand-blue)" stroke-width="0.8"/></svg>
        www.trquillarisadvisory.solutions
      </span>
      <span class="contact-item">
        <svg viewBox="0 0 12 12"><rect x="1" y="3" width="10" height="7" fill="none" stroke="var(--brand-blue)"/><path d="M1 3l5 4 5-4" fill="none" stroke="var(--brand-blue)"/></svg>
        info@trquillarisadvisory.solutions
      </span>
    </div>
    <div class="contact-row">
      <span class="contact-item">
        <svg viewBox="0 0 12 12"><path d="M3 1h2l1 3-1.5 1a6 6 0 0 0 2.5 2.5L8 6l3 1v2a2 2 0 0 1-2 2A8 8 0 0 1 1 3a2 2 0 0 1 2-2z" fill="var(--brand-blue)"/></svg>
        Petra Hallum: 582 901 7763
      </span>
      <span class="contact-item">
        <svg viewBox="0 0 12 12"><path d="M3 1h2l1 3-1.5 1a6 6 0 0 0 2.5 2.5L8 6l3 1v2a2 2 0 0 1-2 2A8 8 0 0 1 1 3a2 2 0 0 1 2-2z" fill="var(--brand-blue)"/></svg>
        Owen Vrastik: 614 825 0397
      </span>
    </div>
  </div>

  <svg class="footer-rules" viewBox="0 0 608 120" aria-hidden="true">
    <g stroke="var(--brand-blue)" stroke-width="1.6" fill="none">
      <line x1="560" y1="78" x2="418" y2="78"/>
      <line x1="560" y1="88" x2="310" y2="88"/>
      <line x1="560" y1="98" x2="200" y2="98"/>
    </g>
  </svg>
</main>
</body>
</html>
```